Security business needs NDA formatted.

We need our NDA formatted properly and to look modern with our logo. Anybody can paste words into a document, but we need something clean, modern, DocuSign-friendly, and stylish.

```html
<!DOCTYPE html>
<html lang="en">
<head>
<meta charset="utf-8">
<title>Terravance Non-Disclosure Agreement</title>
<link href="https://fonts.googleapis.com/css2?family=Carlito:wght@400;700&display=swap" rel="stylesheet">
<style>
:root{
  --bg:#cbcbcb;
  --paper:#ffffff;
  --ink:#1a1a1a;
  --band:#000000;
  --rule:#9a9a9a;
  --muted:#6b6b6b;
}
*{box-sizing:border-box;margin:0;padding:0}
html,body{width:1200px;height:789px;overflow:hidden;background:var(--bg)}
body{position:relative;font-family:"Carlito",Calibri,sans-serif;color:var(--ink)}
.page{position:absolute;width:255px;height:330px;background:var(--paper);overflow:hidden}
.page::before{content:"";position:absolute;left:0;top:0;width:18px;height:100%;background:var(--band)}
.brand{position:absolute;left:9px;top:12px;display:flex;align-items:center}
.brand-dot{width:17px;height:17px;border-radius:50%;background:var(--band)}
.brand-name{margin-left:4px;font-family:"Carlito",Calibri,sans-serif;font-weight:700;font-size:8px;line-height:9px;color:var(--ink)}
.brand-rule{position:absolute;left:71px;right:34px;top:22px;height:.5px;background:var(--rule)}
.body{position:absolute;left:30px;right:31px;top:37px;font-size:4.55px;line-height:6.05px;text-align:justify}
.footer{position:absolute;left:30px;right:31px;bottom:24px;border-top:.4px solid #dcdcdc;padding-top:3px;text-align:right;font-family:"Times New Roman",serif;font-size:4px;color:var(--muted);letter-spacing:.4px}
h1{font-weight:700;font-size:6.3px;text-align:center;margin:20px 0 6px;font-variant:small-caps;letter-spacing:.1px}
h2{font-weight:700;font-size:4.55px;margin:5px 0 5px;text-transform:uppercase}
p{margin-bottom:5px}
.c{text-align:center}
.r{text-align:right}
.cl{position:relative;padding-left:15px;margin-bottom:5px}
.cl>.n{position:absolute;left:0}
.sub{position:relative;padding-left:30px;margin-bottom:5px}
.sub>.n{position:absolute;left:15px}
.sub3{position:relative;padding-left:56px;margin-bottom:5px}
.sub3>.n{position:absolute;left:44px}
.sign{margin-left:105px;margin-bottom:8px;text-align:left}
.copy{position:absolute;left:30px;bottom:36px;font-family:Arial,sans-serif;font-size:2.4px;line-height:3px}
</style>
</head>
<body>

<section class="page" style="left:61px;top:38px">
  <div class="brand"><div class="brand-dot"></div><div class="brand-name">Terravance</div></div>
  <div class="brand-rule"></div>
  <div class="body">
    <h1>Non-Disclosure Agreement</h1>
    <p style="padding-left:2px"><b>THIS NON-DISCLOSURE AGREEMENT</b> ("the Agreement") dated this_________day of _____________________.</p>
    <p class="c" style="margin-top:25px;font-weight:700">BETWEEN</p>
    <p class="c" style="margin-bottom:0">ACME of 88 Harbor Lane, CA, 95010, USA</p>
    <p class="c">(the "Company")</p>
    <p class="r" style="margin-bottom:20px">OF THE FIRST PART</p>
    <p class="c" style="font-weight:700">AND</p>
    <p class="c" style="margin-bottom:7px">COMPANY NAME of COMPANY ADDRESS</p>
    <p class="c" style="margin-bottom:7px">(the "Evaluator")</p>
    <p class="r">OF THE SECOND PART</p>
    <h2>Background</h2>
    <div class="cl" style="margin-left:2px"><span class="n">A.</span>ACME has proprietary information and know-how relating to certain investigation tools and tactics (the "Company").</div>
    <div class="cl" style="margin-left:2px"><span class="n">B.</span>In connection with the Evaluator evaluating the Invention for possible patent, development, and marketing (the "Permitted Purpose"), the Evaluator has requested certain confidential information (the "Confidential Information") regarding the Company.</div>
    <p style="padding-left:2px"><b>IN CONSIDERATION OF</b> and as a condition of the Company providing the Confidential Information to the Evaluator in addition to other valuable consideration, the receipt and sufficiency of which consideration is hereby acknowledged, the parties to this Agreement agree as follows:</p>
  </div>
  <div class="footer">1 | Page</div>
</section>

<section class="page" style="left:339px;top:38px">
  <div class="brand"><div class="brand-dot"></div><div class="brand-name">Terravance</div></div>
  <div class="brand-rule"></div>
  <div class="body">
    <h2 style="margin-top:0">Confidential Information</h2>
    <div class="cl"><span class="n">1.</span>All written and oral information and materials disclosed or provided by the Company to the Evaluator under this Agreement constitute Confidential Information regardless of whether such information was provided before or after the date of this Agreement or how it was provided to the Evaluator.</div>
    <div class="cl"><span class="n">2.</span>'Confidential Information' means all data and information relating to the invention as well as data and information relating to the Company, including but not limited to, the following:</div>
    <div class="sub"><span class="n">a.</span>'Business Operations' which includes internal personnel and financial information of the Company, vendor names and other vendor information (including vendor characteristics, services and agreements), purchasing and internal cost information, internal services and operational manuals, external business contacts including those stored on social media accounts or other similar platforms or databases operated by the Company, and the manner and methods of conducting the Company's business;</div>
    <div class="sub"><span class="n">b.</span>'Customer Information' which includes names of customers of the Company, their representatives, all customer contact information, contracts and their contents and parties, customer services, data provided by customers and the type, quantity and specifications of products and services purchased, leased, licensed or received by customers of the Company;</div>
    <div class="sub"><span class="n">c.</span>'Intellectual Property' which includes information relating to the Company's proprietary rights prior to any public disclosure of such information, including but not limited to the nature of the proprietary rights, production data, technical and engineering data, technical concepts, test data and test results, simulation results, the status and details of research and development of products and services, and information regarding acquiring, protecting, enforcing and licensing proprietary rights (including patents, copyrights and trade secrets);</div>
    <div class="sub"><span class="n">d.</span>'Service Information' which includes all data and information relating to the services provided by the Company, including but not limited to, plans, schedules, manpower, inspection, and training information;</div>
    <div class="sub"><span class="n">e.</span>'Product Information' which includes all specifications for products of the Company as well as work product resulting from or related to work or projects of the Company, of any type or form in any stage of actual or anticipated research and development;</div>
    <div class="sub"><span class="n">f.</span>'Production Processes' which includes processes used in the creation, production and manufacturing of the work product of the Company, including but not</div>
  </div>
  <div class="footer">2 | Page</div>
</section>

<section class="page" style="left:617px;top:38px">
  <div class="brand"><div class="brand-dot"></div><div class="brand-name">Terravance</div></div>
  <div class="brand-rule"></div>
  <div class="body">
    <div class="sub">limited to, formulas, patterns, molds, models, methods, techniques, specifications, processes, procedures, equipment, devices, programs, and designs;</div>
    <div class="sub"><span class="n">g.</span>'Accounting Information' which includes, without limitation, all financial statements, annual reports, balance sheets, company asset information, company liability information, revenue and expense reporting, profit and loss reporting, cash flow reporting, accounts receivable, accounts payable, Company reporting, purchasing information and payroll information of the Company;</div>
    <div class="sub"><span class="n">h.</span>'Marketing and Development Information' which includes marketing and development plans of the Company, price and cost data, price and fee amounts, pricing and billing policies, quoting procedures, marketing techniques and methods of obtaining business, forecasts and forecast assumptions and volumes, and future plans and potential strategies of the Company which have been or are being discussed;</div>
    <div class="sub"><span class="n">i.</span>'Computer Technology' which includes all scientific and technical information or material of the Company, pertaining to any machine, appliance or process, including but not limited to, specifications, proposals, models, designs, formulas, test results and reports, analyses, simulation results, tables of operating conditions, materials, components, industrial skills, operating and testing procedures, shop practices, know-how and show-how;</div>
    <div class="sub"><span class="n">j.</span>'Proprietary Computer Code' which includes all sets of statements, instructions or programs of the Company, whether in human readable or machine readable form, that are expressed, fixed, embodied or stored in any manner and that can be used directly or indirectly in a computer ('Computer Programs'); any report format, design or drawing created or produced by such Computer Programs; and all documentation, design specifications and charts, and operating procedures which support the Computer Programs; and</div>
    <div class="sub"><span class="n">k.</span>Confidential Information will also include any information that has been disclosed by a third party to the Company and is protected by a non-disclosure agreement entered into between the third party and the Company.</div>
    <div class="cl" style="margin-left:2px"><span class="n">3.</span>Confidential Information will not include the following information</div>
    <div class="sub"><span class="n">a.</span>Information that is generally known in the industry of the Company;</div>
    <div class="sub"><span class="n">b.</span>Information that is now or subsequently becomes generally available to the public through no wrongful act of the Evaluator;</div>
  </div>
  <div class="footer">3 | Page</div>
</section>

<section class="page" style="left:895px;top:38px">
  <div class="brand"><div class="brand-dot"></div><div class="brand-name">Terravance</div></div>
  <div class="brand-rule"></div>
  <div class="body">
    <div class="sub"><span class="n">c.</span>Information rightly in the possession of the Evaluator prior to the disclosure to the Evaluator by the Company;</div>
    <div class="sub"><span class="n">d.</span>Information that is independently created by the Evaluator without direct or indirect use of the Confidential Information; or</div>
    <div class="sub"><span class="n">e.</span>Information that the Evaluator rightfully obtains from a third party who has the right to transfer or disclose it.</div>
    <h2>Obligations of Non-Disclosure</h2>
    <div class="cl"><span class="n">4.</span>Except as otherwise provided in this Agreement, the Evaluator must not disclose the Confidential Information.</div>
    <div class="cl"><span class="n">5.</span>Except as otherwise provided in this Agreement, the Confidential Information will remain the exclusive property of the Company and will only be used by the Evaluator for the Permitted Purpose. The Evaluator will not use the Confidential Information for any purpose that might be directly or indirectly detrimental to the Company or any associated affiliates or subsidiaries.</div>
    <div class="cl"><span class="n">6.</span>The obligations to ensure and prevent the disclosure of the Confidential Information imposed on the Evaluator in this Agreement and any obligations to provide notice under this Agreement will survive the expiration or termination, as the case may be, of this Agreement and those obligations will last indefinitely.</div>
    <div class="cl"><span class="n">7.</span>The Evaluator may disclose any of the Confidential Information:</div>
    <div class="sub"><span class="n">a.</span>to such employees, agents, representatives and advisors of the Evaluator that have a need to know for the Permitted Purpose provided that:</div>
    <div class="sub3"><span class="n">i.</span>the Evaluator has informed such personnel of the confidential nature of the Confidential Information;</div>
    <div class="sub3"><span class="n">ii.</span>such personnel agree to be legally bound to the same burdens of non-disclosure and non-use as the Evaluator;</div>
    <div class="sub3"><span class="n">iii.</span>the Evaluator agrees to take all necessary steps to ensure that the terms of this Agreement are not violated by such personnel; and</div>
    <div class="sub3"><span class="n">iv.</span>the Evaluator agrees to be responsible for and indemnify the Company for any breach of this Agreement by its personnel.</div>
    <div class="sub"><span class="n">b.</span>to a third party where the Company has consented in writing to such disclosure; and</div>
  </div>
  <div class="footer">4 | Page</div>
</section>

<section class="page" style="left:61px;top:403px">
  <div class="brand"><div class="brand-dot"></div><div class="brand-name">Terravance</div></div>
  <div class="brand-rule"></div>
  <div class="body">
    <div class="sub"><span class="n">c.</span>to the extent required by law or by the request or requirement of any judicial, legislative, administrative or other governmental body.</div>
    <div class="cl"><span class="n">8.</span>The Evaluator agrees to retain all Confidential Information at its usual place of business and to store all Confidential Information separate from other information and documents held in the same location. Further, the Confidential Information may not be used, reproduced, transformed, or stored on a computer or device that is accessible to persons to whom disclosure may not be made, as set out in this Agreement.</div>
    <h2>Non-Solicitation</h2>
    <div class="cl"><span class="n">9.</span>The Evaluator, its affiliates, subsidiaries and representatives will not, from the date of this Agreement for a period of two years, directly or indirectly solicit for employment or employ any person who is now employed or retained by the Company or any affiliate of the Company without the prior written consent of the Company.</div>
    <h2>Non-Competition</h2>
    <div class="cl"><span class="n">10.</span>Other than with the express written consent of the Company, which consent may not be unreasonably withheld, the Evaluator will not, from the date of this Agreement for a period of two years, be directly or indirectly involved with a business which is in direct competition with the Company in the market for the Invention.</div>
    <h2>Ownership and Title</h2>
    <div class="cl"><span class="n">11.</span>Nothing contained in this Agreement will grant to or create in the Evaluator, either expressly or impliedly, any right, title, interest or license in or to the intellectual property of the Company.</div>
    <h2>Remedies</h2>
    <div class="cl"><span class="n">12.</span>The Evaluator agrees and acknowledges that the Confidential Information is of a proprietary and confidential nature and that any disclosure of the Confidential Information to a third party in breach of this Agreement cannot be reasonably or adequately compensated for in money damages and would cause irreparable injury to the Company. Accordingly, the Evaluator agrees that the Company is entitled to, in addition to all other rights and remedies available to it at law or in equity, an injunction restraining the Evaluator, any of its personnel, and any agents of the Evaluator, from directly or indirectly committing or engaging in any act restricted by this Agreement in relation to the Confidential Information.</div>
    <h2>Return of Confidential Information</h2>
    <div class="cl"><span class="n">13.</span>The Company may at any time request the return of all Confidential Information from the Evaluator. Upon the request of the Company, or in the event that the Evaluator</div>
  </div>
  <div class="footer">5 | Page</div>
</section>

<section class="page" style="left:339px;top:403px">
  <div class="brand"><div class="brand-dot"></div><div class="brand-name">Terravance</div></div>
  <div class="brand-rule"></div>
  <div class="body">
    <div class="cl">ceases to require use of the Confidential Information, or upon the expiration or termination of this Agreement, the Evaluator will:</div>
    <div class="sub"><span class="n">a.</span>return all Confidential Information to the Company;</div>
    <div class="sub"><span class="n">b.</span>provide a certificate to the Company to the effect that the Evaluator has returned all Confidential Information to the Company.</div>
    <h2>Notices</h2>
    <div class="cl"><span class="n">14.</span>In the event that the Evaluator is required in a civil, criminal or regulatory proceeding to disclose any part of the Confidential Information, the Evaluator will give to the Company prompt written notice of such request so the Company may seek an appropriate remedy or alternatively to waive the Evaluator's compliance with the provisions of this Agreement in regards to the request.</div>
    <div class="cl"><span class="n">15.</span>If the Evaluator loses or makes unauthorized disclosure of any of the Confidential Information, the Evaluator will immediately notify the Company and take all reasonable steps necessary to retrieve the lost or improperly disclosed Confidential Information.</div>
    <div class="cl"><span class="n">16.</span>Any notices or delivery required in this Agreement will be deemed completed when hand- delivered, delivered by agent, or seven days after being placed in the post, postage prepaid, to the parties at the addresses contained in this Agreement or as the parties may later designate in writing.</div>
    <div class="cl"><span class="n">17.</span>The addresses for any notice to be delivered to any of the parties to this Agreement are as follows:</div>
    <div class="sub"><span class="n">a.</span>Name: ACME<br>Address: 1520 Orchard Ave, Lansing, MI 48906, USA</div>
    <div class="sub"><span class="n">b.</span>Name: COMPANY NAME Address: COMPANY ADDRESS</div>
    <h2>Representations</h2>
    <div class="cl"><span class="n">18.</span>In providing the Confidential Information, the Company makes no representations, either expressly or impliedly as to its adequacy, sufficiency, completeness, correctness or its lack of defect of any kind, including any patent or trademark infringement that may result from the use of such information.</div>
    <h2>Further Agreements</h2>
    <div class="cl"><span class="n">19.</span>In the event that the Evaluator finds that the Invention is worthy of being patented, developed and marketed, the Company and the Evaluator may negotiate an additional agreement to define all their respective rights regarding such patenting, marketing, and</div>
  </div>
  <div class="footer">6 | Page</div>
</section>

<section class="page" style="left:617px;top:403px">
  <div class="brand"><div class="brand-dot"></div><div class="brand-name">Terravance</div></div>
  <div class="brand-rule"></div>
  <div class="body">
    <div class="cl">development.</div>
    <h2>Termination</h2>
    <div class="cl"><span class="n">20.</span>Either party may terminate this Agreement by providing written notice to the other party. Except as otherwise provided in this Agreement, all rights and obligations under this Agreement will terminate at that time.</div>
    <h2>Assignment</h2>
    <div class="cl"><span class="n">21.</span>Except where a party has changed its corporate name or merged with another corporation, this Agreement may not be assigned or otherwise transferred by either party in whole or part without the prior written consent of the other party to this Agreement.</div>
    <h2>Amendments</h2>
    <div class="cl"><span class="n">22.</span>This Agreement may only be amended or modified by a written instrument executed by both the Company and the Evaluator.</div>
    <h2>Governing Law</h2>
    <div class="cl"><span class="n">23.</span>This Agreement will be construed in accordance with and governed by the laws of the State of Michigan.</div>
    <h2>General Provisions</h2>
    <div class="cl"><span class="n">24.</span>Time is of the essence in this Agreement.</div>
    <div class="cl"><span class="n">25.</span>This Agreement may be executed in counterpart.</div>
    <div class="cl"><span class="n">26.</span>Headings are inserted for the convenience of the parties only and are not to be considered when interpreting this Agreement. Words in the singular mean and include the plural and vice versa. Words in the masculine mean and include the feminine and vice versa.</div>
    <div class="cl"><span class="n">27.</span>The clauses, paragraphs, and subparagraphs contained in this Agreement are intended to be read and construed independently of each other. If any part of this Agreement is held to be invalid, this invalidity will not affect the operation of any other part of this Agreement.</div>
    <div class="cl"><span class="n">28.</span>The Evaluator is liable for all costs, expenses and expenditures including, and without limitation, the complete legal costs incurred by the Company in enforcing this Agreement as a result of any default of this Agreement by the Evaluator.</div>
  </div>
  <div class="footer">7 | Page</div>
</section>

<section class="page" style="left:895px;top:403px">
  <div class="brand"><div class="brand-dot"></div><div class="brand-name">Terravance</div></div>
  <div class="brand-rule"></div>
  <div class="body">
    <div class="cl"><span class="n">29.</span>The Company and the Evaluator acknowledge that this Agreement is reasonable, valid and enforceable. However, if a court of competent jurisdiction finds any of the provisions of this Agreement to be too broad to be enforceable, it is the intention of the Company and the Evaluator that such provision be reduced in scope by the court only to the extent deemed necessary by that court to render the provision reasonable and enforceable, bearing in mind that it is the intention of the Evaluator to give the Company the broadest possible protection against disclosure of the Confidential Information.</div>
    <div class="cl"><span class="n">30.</span>No failure or delay by the Company in exercising any power, right or privilege provided in this Agreement will operate as a waiver, nor will any single or partial exercise of such rights, powers or privileges preclude any further exercise of them or the exercise of any other right, power or privilege provided in this Agreement.</div>
    <div class="cl"><span class="n">31.</span>This Agreement will inure to the benefit of and be binding upon the respective heirs, executors, administrators, successors and assigns, as the case may be, of the Company and the Evaluator.</div>
    <div class="cl"><span class="n">32.</span>This Agreement constitutes the entire agreement between the parties and there are no further items or provisions, either oral or otherwise.</div>
    <p style="margin-bottom:12px"><b>IN WITNESS WHEREOF</b> ACME and COMPANY NAME have duly affixed their signatures under hand and seal on this _______________day of _________________, _________.</p>
    <div class="sign">ACME<br>Per:___________________________ (Seal)</div>
    <div class="sign" style="margin-top:12px">COMPANY NAME<br>Per:___________________________ (Seal)</div>
  </div>
  <div class="copy">©2002-2022<br>FormLedger.com®</div>
  <div class="footer">8 | Page</div>
</section>

</body>
</html>
```